Ferncrest Dental, LLC business card project

Business card to be designed with current logo.
Dental office- please keep design of card that looks clean and professional.
Please include the following info:
Ferncrest Dental, LLC
Dr. Lorna Pettigrew
2871 Marlowe Street
Alderbrook, OH 43999
555-555-0193
ferncrestdental.office@examplemail.test
Hello everyone-
Reason: Just got back from overseas- will look at all designs and provide feedback. Thank you!
Reason: Polling my friends for the final selection-
thank you to all those that participated- so many talented designers!

```html
<!DOCTYPE html>
<html lang="en">
<head>
<meta charset="utf-8">
<title>Ferncrest Dental, LLC – Business Card</title>
<link rel="stylesheet" href="https://fonts.googleapis.com/css2?family=Arimo:wght@400&display=swap">
<style>
  :root {
    --card-bg: #ffffff;
    --brand-green: #62a03c;
    --brand-green-light: #a6cf3a;
    --name-ink: #474747;
    --detail-ink: #868686;
    --bar-green: #5e9b3a;
  }
  html, body {
    margin: 0;
    padding: 0;
    width: 1200px;
    height: 686px;
    overflow: hidden;
    background: var(--card-bg);
  }
  .card {
    position: relative;
    width: 1200px;
    height: 686px;
    background: var(--card-bg);
    font-family: "Arimo", Arial, sans-serif;
    overflow: hidden;
  }
  .brand {
    position: absolute;
    top: 46px;
    right: 28px;
    display: flex;
    align-items: center;
    gap: 22px;
  }
  .brand-dot {
    width: 58px;
    height: 58px;
    border-radius: 50%;
    background: var(--brand-green-light);
  }
  .brand-name {
    margin: 0;
    font-size: 78px;
    font-weight: 400;
    line-height: 1;
    letter-spacing: -0.5px;
    color: var(--brand-green);
    white-space: nowrap;
  }
  .doctor-name {
    position: absolute;
    left: 25px;
    top: 370px;
    margin: 0;
    font-size: 58px;
    font-weight: 400;
    line-height: 1;
    color: var(--name-ink);
  }
  .contact {
    position: absolute;
    left: 25px;
    top: 485px;
    margin: 0;
    font-style: normal;
    font-size: 38px;
    line-height: 45.5px;
    color: var(--detail-ink);
  }
  .contact span { display: block; }
  .base-bar {
    position: absolute;
    left: 0;
    bottom: 0;
    width: 1200px;
    height: 10px;
    background: var(--bar-green);
  }
</style>
</head>
<body>
  <main class="card">
    <header class="brand">
      <span class="brand-dot" aria-hidden="true"></span>
      <h1 class="brand-name">Ferncrest Dental</h1>
    </header>

    <h2 class="doctor-name">Dr. Lorna Pettigrew</h2>

    <address class="contact">
      <span class="contact-street">2871 Marlowe Street</span>
      <span class="contact-city">Alderbrook, OH 43999</span>
      <span class="contact-phone">555-555-0193</span>
      <span class="contact-email">ferncrestdental.office@examplemail.test</span>
    </address>

    <div class="base-bar" aria-hidden="true"></div>
  </main>
</body>
</html>
```